Hotel Lobby sign up to invest banner 4ft by 8 ft

We need to have a 4ft x 8ft banner designed. the sign is to attract investors to purchase condos at The Lodge at Marlowe's Bend. Banner will hang in lobby and an ipad will be available for guest to sign up to get information and investor information.
The wording used should be something similar to or:

You Love the Resort, why not own it?

Sign-Up Here to receive updates & new condo information

Target Market(s)

Condo guest looking to invest

Industry/Entity Type

Hospitality

Requirements
Must have
• Logo and be 4ft by 8 ft
Nice to have
• use the attached map but does not have to
• font has to be eligible
Should not have
• scripted font

```html
<!DOCTYPE html>
<html lang="en">
<head>
<meta charset="utf-8">
<title>The Lodge at Marlowe's Bend – Lobby Investor Banner</title>
<link rel="stylesheet" href="https://fonts.googleapis.com/css2?family=Playfair+Display:wght@900&family=Poppins:wght@300;500&display=swap">
<style>
  :root {
    --ink: #0b0b0b;
    --gold: #d2a062;
    --gold-deep: #c8945a;
    --white: #ffffff;
    --text-dark: #1c1a17;
    --photo-dark: #141414;
    --photo-mid: #3a3a3a;
  }
  * { margin: 0; padding: 0; box-sizing: border-box; }
  html, body {
    width: 1200px;
    height: 2400px;
    overflow: hidden;
    background: var(--ink);
  }
  .banner {
    position: relative;
    width: 1200px;
    height: 2400px;
    background: var(--ink);
    overflow: hidden;
  }
  .hero-photo {
    position: absolute;
    left: 0; top: 0;
    width: 1200px;
    height: 1080px;
    background: radial-gradient(ellipse 45% 40% at 52% 30%, #8a7e74 0%, var(--photo-mid) 40%, var(--photo-dark) 80%);
  }
  .shapes {
    position: absolute;
    left: 0; top: 0;
    width: 1200px;
    height: 2400px;
  }
  .headline {
    position: absolute;
    left: 0; top: 0;
    width: 1200px;
    height: 2400px;
    font-family: "Playfair Display", Georgia, serif;
    font-weight: 900;
    color: var(--gold);
  }
  .headline span {
    position: absolute;
    line-height: 1;
    white-space: nowrap;
  }
  .headline .word-you {
    left: 62px;
    top: 1132px;
    font-size: 92px;
    transform: rotate(-90deg);
    transform-origin: center;
  }
  .headline .word-love {
    left: 206px;
    top: 1010px;
    font-size: 268px;
    letter-spacing: -4px;
  }
  .headline .word-the {
    left: 800px;
    top: 1140px;
    font-size: 140px;
  }
  .headline .word-resort {
    left: 140px;
    top: 1222px;
    font-size: 262px;
    letter-spacing: -3px;
  }
  .tagline {
    position: absolute;
    left: 0;
    top: 1518px;
    width: 1200px;
    text-align: center;
    font-family: "Poppins", "Century Gothic", sans-serif;
    font-weight: 300;
    font-size: 124px;
    line-height: 1;
    color: var(--white);
  }
  .brand-name {
    position: absolute;
    left: 0;
    top: 1790px;
    width: 1200px;
    text-align: center;
    font-family: "Playfair Display", Georgia, serif;
    font-weight: 900;
    font-size: 64px;
    line-height: 1.15;
    color: var(--gold);
  }
  .signup-call {
    position: absolute;
    left: 0;
    top: 2180px;
    width: 1200px;
    text-align: center;
    font-family: "Poppins", Arial, sans-serif;
    font-weight: 500;
    font-size: 58px;
    line-height: 1.4;
    color: var(--text-dark);
  }
</style>
</head>
<body>
<main class="banner">
  <div class="hero-photo" role="img" aria-label="Photo of a man in a dark suit and white shirt reaching out his hand for a handshake"></div>

  <svg class="shapes" viewBox="0 0 1200 2400" width="1200" height="2400" aria-hidden="true">
    <polygon class="gold-chevron" fill="var(--gold)" points="0,720 660,960 1200,840 1200,950 660,1070 0,818"/>
    <polygon class="dark-panel" fill="var(--ink)" points="0,818 660,1070 1200,950 1200,2400 0,2400"/>
    <polygon class="gold-footer" fill="var(--gold)" points="0,1920 624,2112 1200,1896 1200,2400 0,2400"/>
  </svg>

  <h1 class="headline">
    <span class="word-you">You</span>
    <span class="word-love">Love</span>
    <span class="word-the">the</span>
    <span class="word-resort">Resort</span>
  </h1>

  <p class="tagline">why not own it?</p>

  <p class="brand-name">The Lodge at<br>Marlowe's Bend</p>

  <p class="signup-call">Sign-Up Here to receive<br>updates &amp;new condo information</p>
</main>
</body>
</html>
```